Business Card and Stationary Design

After the successful redesign of our logo we are wanting to follow suite and create a new business card and stationary design!

New Logo is attached, information required on the business card should contain a mixture of the following but layout/arrangement is up to the designer.

Happy if the national provider number and abn are on the back, and happy for them to be smaller than the rest.

I am also happy to receive single sided or weird and wonderful designs.

Name
Title
National Provider Number 7291
ABN 53 219 864 317
Level 3, 42 Marlow Street
Kelmarsh NSW 2391
Ph: 1300 987 214
Mobile: 0432 785 619
name@ferngatebuild.com.au
www.ferngatebuild.com.au

Target Market(s)

Professionals, Peers, Students, Suppliers...

Industry/Entity Type

Construction

Contact Information for Business Card

Listed in project description

Font styles to use
Other font styles liked:
• Century Gothic

Colors
0455a3
3176b5
ffffff

Requirements
Must have
• Professional Design, same color scheme as our logo
Nice to have
• Something that sets our apart from everyone else would be fantastic, open to size and shape and layout options, as long as they present professionally.
• Open to raised/embossed text, alternative materials, custom sizes, clear material
Should not have
• The color orange

```html
<!DOCTYPE html>
<html lang="en">
<head>
<meta charset="utf-8">
<title>Ferngatebuild Business Card</title>
<link href="https://fonts.googleapis.com/css2?family=Didact+Gothic&display=swap" rel="stylesheet">
<style>
  :root {
    --stage: #2b2827;
    --paper: #ffffff;
    --brand-blue: #233f8c;
    --logo-blue: #1f3a86;
    --rule-grey: #8d9099;
    --icon-grey: #7d7f86;
    --ink-light: #ffffff;
  }
  * { margin: 0; padding: 0; box-sizing: border-box; }
  html, body { width: 1200px; height: 716px; overflow: hidden; }
  body {
    background: var(--stage);
    font-family: "Didact Gothic", "Century Gothic", sans-serif;
    position: relative;
  }
  .card {
    position: absolute;
    top: 215px;
    width: 500px;
    height: 286px;
    background: var(--paper);
    overflow: hidden;
  }
  .card--front { left: 60px; }
  .card--back { left: 640px; }

  .brand {
    position: absolute;
    display: flex;
    align-items: center;
    gap: 10px;
    color: var(--logo-blue);
    font-size: 34px;
    letter-spacing: 0.5px;
    white-space: nowrap;
  }
  .brand__square {
    width: 22px; height: 22px;
    background: var(--logo-blue);
  }
  .card--front .brand { left: 150px; top: 40px; }
  .card--back .brand { left: 50%; top: 50%; transform: translate(-50%, -50%); font-size: 38px; }

  .contact-band {
    position: absolute;
    left: 0; top: 132px;
    width: 100%; height: 128px;
    background: var(--brand-blue);
    color: var(--ink-light);
  }
  .grey-rule {
    position: absolute;
    left: 0; top: 260px;
    width: 100%; height: 7px;
    background: var(--rule-grey);
  }
  .person { position: absolute; left: 22px; top: 14px; }
  .person__name {
    font-size: 13px;
    padding-bottom: 2px;
    border-bottom: 1px solid var(--ink-light);
    display: inline-block;
  }
  .person__title { font-size: 10px; margin-top: 2px; }
  .registration {
    position: absolute; left: 22px; top: 66px;
    font-size: 8px; line-height: 1.45;
  }
  .details {
    position: absolute; left: 268px; top: 12px;
    list-style: none;
  }
  .details__row {
    display: flex; align-items: flex-start; gap: 10px;
    margin-bottom: 7px;
    font-size: 11px; line-height: 1.3;
    white-space: nowrap;
  }
  .details__icon {
    flex: none;
    width: 22px; height: 22px;
    background: var(--icon-grey);
    display: flex; align-items: center; justify-content: center;
  }
</style>
</head>
<body>
  <section class="card card--front" aria-label="Business card front">
    <div class="brand"><span class="brand__square"></span><span class="brand__name">ferngatebuild</span></div>

    <div class="contact-band">
      <div class="person">
        <div class="person__name">Mrs Helen Carver</div>
        <div class="person__title">Director</div>
      </div>
      <div class="registration">
        <div>National Provider Number 7291</div>
        <div>ABN 53 219 864 317</div>
      </div>
      <ul class="details">
        <li class="details__row">
          <span class="details__icon">
            <svg width="14" height="14" viewBox="0 0 24 24" aria-hidden="true"><path fill="#fff" d="M6.6 10.8a15 15 0 0 0 6.6 6.6l2.2-2.2c.3-.3.7-.4 1-.2 1.1.4 2.3.6 3.6.6.6 0 1 .4 1 1V20c0 .6-.4 1-1 1A17 17 0 0 1 3 4c0-.6.4-1 1-1h3.5c.6 0 1 .4 1 1 0 1.3.2 2.5.6 3.6.1.3 0 .7-.2 1z"/></svg>
          </span>
          <span>1300 987 214<br>0432 785 619</span>
        </li>
        <li class="details__row">
          <span class="details__icon">
            <svg width="14" height="14" viewBox="0 0 24 24" aria-hidden="true" fill="none" stroke="#fff" stroke-width="1.8"><circle cx="12" cy="12" r="9"/><ellipse cx="12" cy="12" rx="4" ry="9"/><path d="M3 12h18M5 7h14M5 17h14"/></svg>
          </span>
          <span>name@ferngatebuild.com.au<br>www.ferngatebuild.com.au</span>
        </li>
        <li class="details__row">
          <span class="details__icon">
            <svg width="14" height="14" viewBox="0 0 24 24" aria-hidden="true"><path fill="#fff" d="M12 2a7 7 0 0 0-7 7c0 5 7 13 7 13s7-8 7-13a7 7 0 0 0-7-7zm0 9.5A2.5 2.5 0 1 1 12 6.5a2.5 2.5 0 0 1 0 5z"/></svg>
          </span>
          <span>Level 3, 42 Marlow Street<br>Kelmarsh NSW 2391</span>
        </li>
      </ul>
    </div>
    <div class="grey-rule"></div>
  </section>

  <section class="card card--back" aria-label="Business card back">
    <div class="brand"><span class="brand__square"></span><span class="brand__name">ferngatebuild</span></div>
  </section>
</body>
</html>
```